Business card to be used as a flyer

This business card should do the trick of a full scale flyer , so basicaly from the business card itself we only keep the size and remove the clasical name , position , company name (etc).
This business cards should be , like said above, used as promo tool, being gived to different girls . So base one : the design is girls oriented.
Colors : black background . We will use gold (color) folio for the text.
Attached you have our logo, but this should not be a proiminent part of the design . You can use only the cat head instead.
Target Market(s)
Girls / Women
Contact Information for Business Card
> black background , gold / folio text and elements
> cat head from the logo in a creative way do be displayed
> proieminent text "your path to success starts here"
> contact details phone and website .
www.velmastrand.ro (website) and 0742163958 (phone)

```html
<!DOCTYPE html>
<html lang="en">
<head>
<meta charset="utf-8">
<title>Velmastrand – Promo Card</title>
<link rel="stylesheet" href="https://fonts.googleapis.com/css2?family=Yellowtail&display=swap">
<style>
  :root {
    --backdrop: #d9d6d2;
    --card-black: #0b0d16;
    --gold-deep: #8a6410;
    --gold-mid: #d8a92c;
    --gold-light: #fbe27a;
    --gold-text: #e2b548;
  }
  * { margin: 0; padding: 0; box-sizing: border-box; }
  html, body {
    width: 1200px;
    height: 635px;
    overflow: hidden;
    background: var(--backdrop);
  }
  .canvas {
    position: relative;
    width: 1200px;
    height: 635px;
  }
  .promo-card {
    position: absolute;
    left: 150px;
    top: 17px;
    width: 900px;
    height: 600px;
    background: var(--card-black);
    overflow: hidden;
  }
  .gold-art {
    position: absolute;
    left: 0;
    top: 0;
    width: 340px;
    height: 600px;
  }
  .corner-accent {
    position: absolute;
    left: 815px;
    top: 160px;
    width: 70px;
    height: 180px;
  }
  .foil-text {
    font-family: "Yellowtail", cursive;
    background: linear-gradient(180deg, var(--gold-light) 0%, var(--gold-mid) 55%, var(--gold-deep) 100%);
    -webkit-background-clip: text;
    background-clip: text;
    color: transparent;
    white-space: nowrap;
  }
  .headline {
    position: absolute;
    left: 0;
    top: 0;
    font-size: 82px;
    line-height: 1;
    font-weight: 400;
  }
  .headline span {
    position: absolute;
    display: block;
  }
  .headline .line-1 { left: 330px; top: 70px; }
  .headline .line-2 { left: 420px; top: 190px; }
  .headline .line-3 { left: 358px; top: 310px; }
  .contact {
    position: absolute;
    top: 500px;
    display: flex;
    align-items: center;
    gap: 18px;
  }
  .contact-phone { left: 210px; }
  .contact-web { left: 568px; }
  .contact-icon { width: 40px; height: 40px; flex: none; }
  .contact-text {
    font-size: 38px;
    line-height: 1;
    letter-spacing: 1px;
  }
</style>
</head>
<body>
<main class="canvas">
  <section class="promo-card">
    <svg class="gold-art" role="img" aria-label="Gold foil cat head silhouette rising along the left edge" viewBox="0 0 340 600">
      <defs>
        <linearGradient id="foil" x1="0" y1="0" x2="1" y2="1">
          <stop offset="0" stop-color="#7a560c"/>
          <stop offset="0.45" stop-color="#f6d666"/>
          <stop offset="1" stop-color="#c9961c"/>
        </linearGradient>
      </defs>
      <path d="M0 0 H290 C300 140 210 240 205 360 C202 460 222 540 210 600 H0 Z" fill="url(#foil)"/>
      <path d="M300 0 C330 150 232 250 228 370 C225 470 248 540 238 600" fill="none" stroke="url(#foil)" stroke-width="3"/>
    </svg>

    <svg class="corner-accent" role="img" aria-label="Small gold cat ornament" viewBox="0 0 70 180">
      <defs>
        <linearGradient id="foil-small" x1="0" y1="0" x2="0" y2="1">
          <stop offset="0" stop-color="#f6d666"/>
          <stop offset="1" stop-color="#8a6410"/>
        </linearGradient>
      </defs>
      <rect x="10" y="0" width="50" height="180" rx="25" fill="url(#foil-small)" opacity="0.55"/>
    </svg>

    <h1 class="headline foil-text">
      <span class="line-1 foil-text">Your Path to</span>
      <span class="line-2 foil-text">Success</span>
      <span class="line-3 foil-text">Starts Here</span>
    </h1>

    <div class="contact contact-phone">
      <svg class="contact-icon" viewBox="0 0 40 40" aria-hidden="true">
        <circle cx="20" cy="20" r="17" fill="none" stroke="var(--gold-text)" stroke-width="2.5"/>
        <path d="M14 11 l4 0 l1.5 5 l-2.5 2 c1.5 3 3 4.5 5 5.5 l2 -2.5 l5 1.5 l0 4 c-9 1 -16 -6 -15 -15.5 z" fill="var(--gold-text)"/>
      </svg>
      <span class="contact-text foil-text">0742163958</span>
    </div>

    <div class="contact contact-web">
      <svg class="contact-icon" viewBox="0 0 40 40" aria-hidden="true">
        <g fill="none" stroke="var(--gold-text)" stroke-width="2">
          <circle cx="20" cy="20" r="16"/>
          <ellipse cx="20" cy="20" rx="7" ry="16"/>
          <line x1="20" y1="4" x2="20" y2="36"/>
          <line x1="4" y1="20" x2="36" y2="20"/>
          <path d="M7 12 H33 M7 28 H33"/>
        </g>
      </svg>
      <span class="contact-text foil-text">velmastrand.ro</span>
    </div>
  </section>
</main>
</body>
</html>
```